Harrow Glen Whiskey Label

We are looking for a label to be made for our single batch whiskey. in the attached pdf you will see the lay out of the design. We are going to use a whiskey bottle with a cork. Some of the label you will need to leave some space for hand writing.

Target Market(s)

people who like craft beer and whiskey

Industry/Entity Type

Craft Distillery

Font styles to use
Decorative

Colors

Designer to choose colors to be used in the design.

Requirements
Must have
• room for hand writing informatiom

```html
<!DOCTYPE html>
<html lang="en">
<head>
<meta charset="utf-8">
<title>Harrow Glen Whiskey Label</title>
<link href="https://fonts.googleapis.com/css2?family=Crimson+Text:wght@400;700&family=Lobster+Two:wght@700&family=Noto+Sans:wght@400;500;600&display=swap" rel="stylesheet">
<style>
  :root {
    --backdrop: #b4b4b4;
    --label-black: #000000;
    --gold: #ecd98a;
    --gold-band: #d4b842;
    --gold-band-light: #e8d474;
    --ornament-grey: #8a8a8a;
    --field-fill: #b1ac94;
    --field-ink: #1b1b1b;
    --white: #ffffff;
  }
  * { margin: 0; padding: 0; box-sizing: border-box; }
  html, body { width: 1200px; height: 1200px; overflow: hidden; }
  body { background: var(--backdrop); position: relative; }

  .label {
    position: absolute; left: 265px; top: 100px;
    width: 670px; height: 1000px;
    background: var(--label-black);
    color: var(--white);
  }
  .crest-ornament {
    position: absolute; left: 165px; top: 29px; width: 320px; height: 104px;
    background: radial-gradient(ellipse at center, #6e6e6e 0%, #3c3c3c 55%, rgba(0,0,0,0) 75%);
  }
  .brand-name {
    position: absolute; left: 0; right: 0; top: 150px;
    text-align: center;
    font-family: "Crimson Text", serif; font-weight: 700;
    color: var(--gold); font-size: 84px; line-height: 90px;
    padding-left: 30px;
  }
  .divider { position: absolute; left: 88px; width: 494px; height: 14px; }
  .divider--upper { top: 368px; }
  .divider--lower { top: 438px; }
  .cut-name {
    position: absolute; left: 0; right: 0; top: 386px; text-align: center;
    font-family: "Lobster Two", cursive; font-weight: 700; font-size: 38px; line-height: 48px;
  }
  .spirit-line {
    position: absolute; left: 0; right: 0; text-align: center;
    font-family: "Crimson Text", serif; line-height: 1;
  }
  .spirit-line--intro { top: 470px; font-size: 36px; font-weight: 400; }
  .spirit-line--grain { top: 521px; font-size: 42px; font-weight: 700; }

  .field {
    position: absolute; background: var(--field-fill); color: var(--field-ink);
    font-family: "Crimson Text", serif; font-size: 22px;
    padding: 10px 15px;
  }
  .field--source { left: 49px; top: 584px; width: 568px; height: 52px; border-radius: 26px; padding-top: 12px; }
  .field--aged { left: 49px; top: 649px; width: 272px; height: 90px; border-radius: 14px; }
  .field--abv { left: 342px; top: 649px; width: 275px; height: 90px; border-radius: 14px; }
  .field--bottle { left: 49px; top: 749px; width: 568px; height: 75px; border-radius: 14px; padding: 0; }
  .field__half { position: absolute; top: 6px; font-family: inherit; }
  .field__half--left { left: 10px; }
  .field__half--right { left: 292px; }
  .field__split { position: absolute; left: 282px; top: 0; width: 4px; height: 100%; background: var(--label-black); }

  .maker {
    position: absolute; left: 0; right: 0; text-align: center;
    font-family: "Noto Sans", sans-serif; line-height: 1;
  }
  .maker--lead { top: 846px; font-size: 16px; }
  .maker--name { top: 866px; font-size: 24px; font-weight: 600; }
  .maker--address { top: 897px; font-size: 20px; }

  .volume-band {
    position: absolute; left: 0; bottom: 0; width: 670px; height: 53px;
    background: linear-gradient(90deg, var(--gold-band), var(--gold-band-light) 40%, var(--gold-band) 70%, var(--gold-band-light));
  }
  .volume {
    position: absolute; right: 52px; top: 8px;
    font-family: "Noto Sans", sans-serif; font-weight: 500; font-size: 32px; color: #111;
    line-height: 1;
  }
</style>
</head>
<body>
  <main class="label">
    <div class="crest-ornament" role="img" aria-label="Grey scrollwork flourish ornament"></div>

    <div class="brand-name">Ironvale<br>Distillery</div>

    <svg class="divider divider--upper" viewBox="0 0 494 14" aria-hidden="true">
      <line x1="0" y1="7" x2="494" y2="7" stroke="#8a8a8a" stroke-width="2"/>
      <circle cx="20" cy="7" r="4" fill="none" stroke="#8a8a8a" stroke-width="2"/>
      <circle cx="474" cy="7" r="4" fill="none" stroke="#8a8a8a" stroke-width="2"/>
      <circle cx="247" cy="7" r="5" fill="#000" stroke="#8a8a8a" stroke-width="2"/>
    </svg>
    <div class="cut-name">Harrow Glen</div>
    <svg class="divider divider--lower" viewBox="0 0 494 14" aria-hidden="true">
      <line x1="0" y1="7" x2="494" y2="7" stroke="#8a8a8a" stroke-width="2"/>
      <circle cx="20" cy="7" r="4" fill="none" stroke="#8a8a8a" stroke-width="2"/>
      <circle cx="474" cy="7" r="4" fill="none" stroke="#8a8a8a" stroke-width="2"/>
      <circle cx="247" cy="7" r="5" fill="#000" stroke="#8a8a8a" stroke-width="2"/>
    </svg>

    <div class="spirit-line spirit-line--intro">Spirits Distilled from</div>
    <div class="spirit-line spirit-line--grain">Malt Mash and Hops</div>

    <div class="field field--source">Distilate Source:</div>
    <div class="field field--aged">Aged:</div>
    <div class="field field--abv">% Alc. byVol.</div>
    <div class="field field--bottle">
      <span class="field__half field__half--left">Bottle:</span>
      <span class="field__split"></span>
      <span class="field__half field__half--right">Of:</span>
    </div>

    <div class="maker maker--lead">DISTILLED AND BOTTLED BY</div>
    <div class="maker maker--name">IRONVALE DISTILLERY LLC</div>
    <div class="maker maker--address">14 ORCHARD LANE FERNBROOK PA 19040</div>

    <div class="volume-band"><span class="volume">750ml.</span></div>
  </main>
</body>
</html>
```